Termite Mailer September 2021

We need a clean modern looking flyer advertising termites via the mail.

Size should be 9"x6"

Our tagline is "The Smarter Approach to Pest Control"

Something along the stylistic design of these:

https://pics.hollowmarsh.example/Qa83LkTzWp

https://pics.hollowmarsh.example/Rn47VbXcMd

https://pics.hollowmarsh.example/Hj29PsYeUf

https://www.flintquillprint.example/wp-content/uploads/designs/img/Pest-Prevention-Postcard-PST-1003.jpg

Should include some of this verbiage:

HAVE YOU SCHEDULED YOUR ANNUAL TERMITE INSPECTION? - MAKE IT IN RED

DON'T WAIT. PROTECT YOUR HOME TODAY!

ABSOLUTELY FREE INSPECTION. NO OBLIGATION.

TERMITES CAN CAUSE SEVERE DAMAGE TO YOUR HOME.

BRINDLEVALE LOGO

THE SMARTER APPROACH TO PEST CONTROL.

PROTECT YOUR MOST VALUABLE ASSET.

10% DISCOUNT ON ANY SERVICE GUARANTEED IF YOU CALL TODAY.

INCLUDE A PICTURE OF A TERMITE AS WELL SOMEWHERE AND WOOD DAMAGE.

Target Market(s)

Homeowners in Southern California USA

Industry/Entity Type

Pest Control/Extermination

Font styles to use
Other font styles liked:
• Chaparral Pro Italic, Brava Slab

Requirements
Must have
• Clean design, picture of house, picture of Termite, 10% off coupon and call to action on the back
Should not have
• Bad looking houses, colors that don't match our logo

```html
<!DOCTYPE html>
<html lang="en">
<head>
<meta charset="utf-8">
<title>Brindlevale Termite Mailer</title>
<link href="https://fonts.googleapis.com/css2?family=Poppins:wght@500;600;700;800&display=swap" rel="stylesheet">
<style>
  :root {
    --backdrop: #7a7a7a;
    --blue: #0f66b6;
    --blue-dark: #0b57a3;
    --blue-light: #1e7fd6;
    --green: #7cc243;
    --red: #e8321e;
    --ink: #2e2e2e;
    --white: #ffffff;
    --rule: #dcdcdc;
    --stamp: #eceeee;
  }
  * { margin: 0; padding: 0; box-sizing: border-box; }
  html, body {
    width: 953px; height: 1200px; overflow: hidden;
    background: var(--backdrop);
    font-family: "Poppins", sans-serif;
  }
  .card {
    position: absolute; left: 110px; width: 733px; height: 490px;
    background: var(--white); overflow: hidden;
    box-shadow: 6px 8px 10px rgba(0,0,0,.35);
  }
  .card--front { top: 79px; }
  .card--back { top: 642px; }
  .card__art { position: absolute; inset: 0; width: 733px; height: 490px; }
  .txt { position: absolute; line-height: 1; white-space: nowrap; }

  /* front */
  .front__question { left: 32px; top: 24px; color: var(--red); font-weight: 800; font-size: 21.5px; line-height: 1.22; letter-spacing: -.3px; }
  .front__wait { left: 33px; top: 91px; color: var(--white); font-weight: 800; font-size: 32px; letter-spacing: -.5px; }
  .front__protect { left: 33px; top: 129px; color: var(--white); font-weight: 800; font-size: 19.5px; letter-spacing: -.3px; }
  .front__damage { left: 30px; top: 311px; color: var(--ink); font-weight: 700; font-size: 14px; line-height: 1.45; letter-spacing: -.2px; }
  .brand { left: 264px; top: 314px; display: flex; align-items: center; gap: 8px; }
  .brand__dot { width: 46px; height: 46px; border-radius: 50%; background: var(--blue); }
  .brand__name { color: var(--blue); font-weight: 700; font-size: 33px; letter-spacing: -.5px; }
  .front__tagline { left: 234px; top: 393px; color: var(--white); font-weight: 800; font-size: 34px; letter-spacing: -.6px; }
  .front__tagline-strong { left: 234px; top: 429px; color: var(--green); font-weight: 800; font-size: 48px; letter-spacing: -.6px; }

  /* back */
  .back__headline { left: 0; width: 417px; top: 52px; text-align: center; color: var(--white); font-weight: 800; font-size: 26px; line-height: 1.05; letter-spacing: -.6px; }
  .coupon {
    position: absolute; left: 29px; top: 124px; width: 360px; height: 89px;
    background: var(--green); border-radius: 6px;
    box-shadow: 0 10px 8px -6px rgba(0,0,0,.28);
    display: flex; align-items: center;
  }
  .coupon__value { margin-left: 9px; color: var(--white); font-weight: 800; font-size: 70px; letter-spacing: -4px; line-height: 1; }
  .coupon__terms { margin-left: 14px; color: var(--white); font-weight: 800; font-size: 15.5px; line-height: 1.38; letter-spacing: -.3px; }
  .cta {
    position: absolute; left: 65px; top: 337px; width: 288px; height: 39px;
    background: var(--green); border-radius: 6px;
    color: var(--white); font-weight: 700; font-size: 16.5px;
    display: flex; align-items: center; justify-content: center; letter-spacing: -.2px;
  }
  .back__phone { left: 0; width: 417px; top: 393px; text-align: center; color: var(--white); font-weight: 800; font-size: 33px; letter-spacing: -.5px; }
  .back__web { left: 0; width: 417px; top: 430px; text-align: center; color: var(--white); font-weight: 800; font-size: 22px; letter-spacing: -.2px; }
  .stamp { position: absolute; left: 639px; top: 29px; width: 67px; height: 66px; background: var(--stamp); border: 1px solid #cfd2d2; }
  .address-line { position: absolute; left: 480px; width: 226px; height: 1px; background: var(--rule); }
  .return-address { left: 500px; top: 432px; color: var(--ink); font-weight: 500; font-size: 12px; line-height: 1.6; display: flex; gap: 8px; }
</style>
</head>
<body>

<section class="card card--front">
  <svg class="card__art" viewBox="0 0 733 490" aria-hidden="false">
    <defs>
      <linearGradient id="houseTone" x1="0" y1="0" x2="0" y2="1">
        <stop offset="0" stop-color="#6f8fb3"/>
        <stop offset=".45" stop-color="#a8b6c4"/>
        <stop offset=".7" stop-color="#5f8a3c"/>
        <stop offset="1" stop-color="#b7b3ac"/>
      </linearGradient>
      <linearGradient id="termiteTone" x1="0" y1="0" x2="1" y2="1">
        <stop offset="0" stop-color="#a79f87"/>
        <stop offset="1" stop-color="#5a4632"/>
      </linearGradient>
      <linearGradient id="colonyTone" x1="0" y1="0" x2="1" y2="1">
        <stop offset="0" stop-color="#4a3526"/>
        <stop offset=".6" stop-color="#6e4c2f"/>
        <stop offset="1" stop-color="#2e2218"/>
      </linearGradient>
      <radialGradient id="waspTone" cx=".5" cy=".55" r=".6">
        <stop offset="0" stop-color="#e6c430"/>
        <stop offset=".55" stop-color="#8a7a3a"/>
        <stop offset="1" stop-color="#f2f2f2"/>
      </radialGradient>
    </defs>
    <rect class="band band--headline" x="0" y="81" width="420" height="76" fill="var(--blue)"/>
    <polygon points="439,0 733,0 733,270 621,373 505,255 367,111" fill="url(#houseTone)" role="img" aria-label="Photo of a well-kept two-storey home with a lawn and a large ant in the foreground"/>
    <polygon points="0,167 152,167 260,294 0,294" fill="url(#termiteTone)" role="img" aria-label="Close-up photo of a soldier termite on wood"/>
    <polygon points="158,167 400,167 523,294 266,294" fill="url(#colonyTone)" role="img" aria-label="Photo of termites in damaged wood"/>
    <polygon points="0,363 170,363 188,378 0,378" fill="var(--green)"/>
    <polygon points="0,378 236,378 254,490 0,490" fill="url(#waspTone)" role="img" aria-label="Close-up photo of a yellow and black wasp"/>
    <polygon points="236,378 733,378 733,490 254,490" fill="var(--blue-dark)"/>
  </svg>

  <p class="txt front__question">HAVE YOU SCHEDULED YOUR<br>ANNUAL TERMITE INSPECTION?</p>
  <p class="txt front__wait">DON'T WAIT.</p>
  <p class="txt front__protect">PROTECT YOUR HOME TODAY!</p>
  <p class="txt front__damage">TERMITES CAN CAUSE SEVERE<br>DAMAGE TO YOUR HOME.</p>
  <div class="txt brand"><span class="brand__dot"></span><span class="brand__name">BRINDLEVALE</span></div>
  <p class="txt front__tagline">THE SMARTER APPROACH</p>
  <p class="txt front__tagline-strong">TO PEST CONTROL</p>
</section>

<section class="card card--back">
  <svg class="card__art" viewBox="0 0 733 490">
    <defs>
      <radialGradient id="iconTone" cx=".5" cy=".5" r=".5">
        <stop offset="0" stop-color="#8a6a4a"/>
        <stop offset=".45" stop-color="#d9d2c8"/>
        <stop offset="1" stop-color="#ffffff"/>
      </radialGradient>
    </defs>
    <polygon points="0,0 372,0 446,168 0,168" fill="var(--blue-dark)"/>
    <polygon points="345,0 372,0 456,200 446,215" fill="var(--blue-light)"/>
    <polygon points="0,350 424,350 367,490 0,490" fill="var(--blue-dark)"/>

    <g class="no-pest" role="img" aria-label="Mosquito photo crossed out">
      <circle cx="71" cy="278" r="41" fill="url(#iconTone)" stroke="var(--blue)" stroke-width="3"/>
      <line x1="100" y1="249" x2="42" y2="307" stroke="var(--blue)" stroke-width="3"/>
    </g>
    <g class="no-pest" role="img" aria-label="Spider photo crossed out">
      <circle cx="172" cy="278" r="41" fill="url(#iconTone)" stroke="var(--blue)" stroke-width="3"/>
      <line x1="201" y1="249" x2="143" y2="307" stroke="var(--blue)" stroke-width="3"/>
    </g>
    <g class="no-pest" role="img" aria-label="Ant photo crossed out">
      <circle cx="273" cy="278" r="41" fill="url(#iconTone)" stroke="var(--blue)" stroke-width="3"/>
      <line x1="302" y1="249" x2="244" y2="307" stroke="var(--blue)" stroke-width="3"/>
    </g>
    <g class="no-pest" role="img" aria-label="Cockroach photo crossed out">
      <circle cx="374" cy="278" r="41" fill="url(#iconTone)" stroke="var(--blue)" stroke-width="3"/>
      <line x1="403" y1="249" x2="345" y2="307" stroke="var(--blue)" stroke-width="3"/>
    </g>
  </svg>

  <p class="txt back__headline">PROTECT YOUR MOST<br>VALUABLE ASSET.</p>
  <div class="coupon">
    <span class="coupon__value">10%</span>
    <span class="coupon__terms">DISCOUNT ON ANY<br>SERVICE GUARANTEED<br>IF YOU CALL TODAY.</span>
  </div>

  <div class="cta">DON'T DELAY – CALL TODAY</div>
  <svg style="position:absolute;left:195px;top:363px" width="26" height="26" viewBox="0 0 26 26" aria-hidden="true">
    <circle cx="13" cy="13" r="11.5" fill="var(--blue)" stroke="var(--white)" stroke-width="2"/>
    <path d="M9.2 7.5c.5-.4 1.1-.3 1.4.2l1 1.6c.3.5.2 1-.2 1.4l-.6.5c.6 1.3 1.6 2.3 2.9 2.9l.5-.6c.4-.4.9-.5 1.4-.2l1.6 1c.5.3.6.9.2 1.4l-.7.9c-.5.6-1.3.8-2 .5-2.8-1.1-5-3.3-6.1-6.1-.3-.7-.1-1.5.5-2z" fill="var(--white)"/>
  </svg>
  <p class="txt back__phone">714-555-0142</p>
  <p class="txt back__web">www.gobrindlevale.com</p>

  <div class="stamp"></div>
  <div class="address-line" style="top:150px"></div>
  <div class="address-line" style="top:221px"></div>
  <div class="address-line" style="top:291px"></div>

  <div class="txt return-address">
    <svg width="16" height="20" viewBox="0 0 16 20" aria-hidden="true">
      <path d="M8 1a6 6 0 0 0-6 6c0 4.5 6 10 6 10s6-5.5 6-10a6 6 0 0 0-6-6z" fill="var(--green)"/>
      <circle cx="8" cy="7" r="2.3" fill="var(--white)"/>
      <ellipse cx="8" cy="18.3" rx="5" ry="1.2" fill="none" stroke="var(--green)" stroke-width="1.2"/>
    </svg>
    <span>418 W Larkmoor Ave. Unit C<br>&nbsp;&nbsp;&nbsp;&nbsp;&nbsp;Orange, CA 92867</span>
  </div>
</section>

</body>
</html>
```